Criação de Manual da Marca para Viagens & Lazer
A empresa queria:
" Funciona como o uBodal, mas para festas em geral, incluindo festas de pets. O responsável pela festa se cadastra, escolhe o tipo de festa (adulto, teen, infantil, chá de bebê, etc), insere as informações da festa e lança o site no ar. Acoplado a ele está uma lista de presentes ilustrada por produtos reais adequados ao tipo de festa e faixa etária do evento que são conversíveis em créditos. Não há entrega de produto, o total arrecadado é depositado na conta do cliente ou da instituição de caridade por ele indicada. "

```html
<!DOCTYPE html>
<html lang="pt-BR">
<head>
<meta charset="UTF-8">
<title>FestaLista — Manual de Identidade Visual</title>
<link rel="stylesheet" href="https://fonts.googleapis.com/css2?family=Open+Sans:wght@300;400&display=swap">
<style>
  :root {
    --backdrop: #eceded;
    --credit-ink: #6f8294;
    --credit-ink-soft: #8a9aa8;
    --veil: rgba(255, 255, 255, 0.72);
    --cover-top: #e8513f;
    --cover-mid: #ee7130;
    --cover-bottom: #f59a1c;
    --paper-white: #ffffff;
  }
  * { box-sizing: border-box; margin: 0; padding: 0; }
  html, body { width: 1200px; height: 1200px; overflow: hidden; }
  body {
    background: var(--backdrop);
    font-family: "Open Sans", sans-serif;
    display: flex;
    align-items: center;
    justify-content: center;
  }
  .spread {
    display: flex;
    width: 1080px;
    height: 540px;
    box-shadow: 0 18px 40px rgba(0,0,0,0.12);
  }
  .page {
    position: relative;
    width: 540px;
    height: 540px;
    overflow: hidden;
  }
  .page--credits { background: var(--paper-white); }
  .party-photo {
    position: absolute;
    inset: 0;
    background:
      radial-gradient(circle at 18% 12%, rgba(120,190,80,0.55), transparent 22%),
      radial-gradient(circle at 45% 8%, rgba(235,150,200,0.55), transparent 18%),
      radial-gradient(circle at 30% 85%, rgba(250,200,80,0.45), transparent 20%),
      radial-gradient(circle at 75% 80%, rgba(240,120,110,0.35), transparent 22%),
      linear-gradient(180deg, #f2efe9 0%, #f7f4ef 55%, #eef0f4 100%);
  }
  .veil {
    position: absolute;
    left: 0; right: 0;
    top: 60px; bottom: 0;
    background: var(--veil);
    border-top-left-radius: 60% 40px;
    border-top-right-radius: 60% 40px;
  }
  .credits {
    position: absolute;
    left: 0; right: 0;
    top: 150px;
    text-align: center;
    color: var(--credit-ink);
    font-weight: 300;
    font-size: 17px;
    line-height: 1.35;
  }
  .credits__group { margin-bottom: 18px; }
  .credits__role { color: var(--credit-ink-soft); }
  .page--cover {
    background: linear-gradient(180deg, var(--cover-top) 0%, var(--cover-mid) 50%, var(--cover-bottom) 100%);
  }
  .cover__intro {
    position: absolute;
    left: 34px;
    bottom: 40px;
    width: 300px;
    color: var(--paper-white);
    font-weight: 300;
    font-size: 11px;
    line-height: 1.55;
    opacity: 0.92;
  }
</style>
</head>
<body>
  <main class="spread">
    <section class="page page--credits">
      <div class="party-photo" role="img" aria-label="Fotografia de crianças com chapéus de festa coloridos ao redor de uma mesa com toalha de bolinhas"></div>
      <div class="veil"></div>
      <div class="credits">
        <div class="credits__group">
          <p>FestaLista</p>
          <p>Manual de Identidade Visual</p>
        </div>
        <div class="credits__group">
          <p class="credits__role">Diretor</p>
          <p>Helena Prado</p>
        </div>
        <div class="credits__group">
          <p>Projeto de Identidade Visual</p>
          <p>Logo e Web Page Layouts</p>
          <p>Websites e Branding</p>
        </div>
        <div class="credits__group">
          <p class="credits__role">Designers Diretores Responsáveis</p>
          <p>Otávio Reis e Lúcia Reis</p>
        </div>
      </div>
    </section>
    <section class="page page--cover">
      <p class="cover__intro">Projeto de criação de identidade visual para uma plataforma de listas de presentes para festas em geral. O manual reúne as diretrizes de uso da marca, cores, tipografia e aplicações, garantindo uma comunicação clara e alegre em todos os pontos de contato com convidados e anfitriões.</p>
    </section>
  </main>
</body>
</html>
```